Brightwater Systems Website

I am starting an IT consulting business called Brightwater Systems. I recently completed a logo contest on ArtHive and am now looking to put together a basic website. I can provide text and content but am looking for a site design with layout and graphics. I am attaching my logo below. I was thinking of a dark blue and white theme for the website (similar to the logo). However, I am open to ideas. Graphics can be a mix of business and high tech as that is the image I am trying to convey. The site will be relatively simple and probably have only 3 - 5 pages (Home, About Us, Services, Contact, etc.)
Target Market(s)
United States commercial companies and government contractors
Industry/Entity Type
Consulting
Coding
Coded - Design and coding required
Number of Pages Required
4 page
Look and feel

```html
<!DOCTYPE html>
<html lang="en">
<head>
<meta charset="utf-8">
<title>Brightwater Systems — Contact Us</title>
<link href="https://fonts.googleapis.com/css2?family=Oswald:wght@400;500&family=Raleway:wght@400;500&family=Roboto:wght@400;500&display=swap" rel="stylesheet">
<style>
:root{
  --blue:#0557a5;
  --blue-bright:#1a8fd8;
  --navy:#222840;
  --ink:#1d2233;
  --pale:#e8f2f8;
  --line:#d9dde3;
  --muted:#8a8f99;
  --accent-soft:#e3e7f0;
  --white:#ffffff;
}
*{margin:0;padding:0;box-sizing:border-box}
html,body{width:717px;height:1200px;overflow:hidden;background:var(--white)}
body{position:relative;font-family:Roboto,Arial,sans-serif;color:var(--ink)}
.abs{position:absolute}
.site-header{left:0;top:0;width:717px;height:48px;background:var(--white)}
.brand{font-family:Raleway,sans-serif;font-weight:500;color:var(--blue);display:flex;align-items:center;gap:6px}
.brand-dot{width:10px;height:10px;border-radius:50%;background:var(--blue)}
.header-brand{left:85px;top:15px;font-size:14px}
.nav a{position:absolute;font-family:Oswald,sans-serif;font-size:8.5px;font-weight:500;color:var(--ink);text-decoration:none;letter-spacing:.2px;top:19px}
.nav-active{left:583px;top:45px;width:48px;height:3px;background:var(--blue)}
.hero{left:0;top:48px;width:717px;height:233px;background:var(--blue)}
.hero-kicker{left:0;top:119px;width:717px;text-align:center;font-family:Raleway,sans-serif;font-size:13px;color:var(--white)}
.hero-title{left:0;top:140px;width:717px;text-align:center;font-family:Raleway,sans-serif;font-weight:500;font-size:15.5px;color:var(--white)}
.ornament{position:absolute;background:var(--accent-soft)}
.ornament-square{left:656px;top:315px;width:44px;height:44px}
.ornament-tri{left:25px;top:511px;width:40px;height:30px}
.form-card{left:90px;top:206px;width:537px;height:309px;background:var(--white);box-shadow:0 4px 14px rgba(0,0,0,.08)}
.form-frame{left:107px;top:223px;width:503px;height:274px;border:1px solid var(--blue);border-radius:3px}
.field{position:absolute;border:1px solid var(--line);border-radius:3px;background:var(--white);font-size:6px;color:var(--muted);padding:8px 11px}
.captcha{left:125px;top:404px;width:136px;height:34px;border:1px solid var(--line);background:#f9f9f9;box-shadow:0 1px 2px rgba(0,0,0,.1);font-size:5.5px;color:#333}
.captcha-box{left:7px;top:10px;width:12px;height:12px;border:1px solid #bbb;background:var(--white);border-radius:2px}
.captcha-label{left:24px;top:13px}
.captcha-mark{left:112px;top:6px;width:12px;height:12px;background:#c7d3e6}
.captcha-note{left:101px;top:21px;font-size:3.5px;color:#777;text-align:center;width:32px}
.btn{position:absolute;background:var(--blue);color:var(--white);font-family:Oswald,sans-serif;font-size:8.5px;border-radius:20px;display:flex;align-items:center;justify-content:center}
.contact-band{left:0;top:552px;width:717px;height:184px;background:var(--pale)}
.info-card{position:absolute;top:589px;width:132px;height:111px;background:var(--blue);color:var(--white);text-align:center}
.info-card::after{content:"";position:absolute;left:6px;top:8px;right:6px;bottom:6px;border:1px solid var(--white)}
.info-icon{position:absolute;left:0;top:26px;width:100%;display:flex;justify-content:center}
.info-title{position:absolute;top:44px;width:100%;font-family:Oswald,sans-serif;font-size:8px;font-weight:500}
.info-text{position:absolute;top:63px;width:100%;font-size:6px;line-height:13px;padding:0 12px}
.social{position:absolute;top:65px;left:0;width:100%;display:flex;justify-content:center;gap:9px;font-size:6.5px;font-weight:500}
.map{left:0;top:736px;width:717px;height:215px;background:linear-gradient(135deg,#eef0ec 0%,#e9eaea 45%,#f2ecdf 70%,#e3eedd 100%)}
.footer{left:0;top:951px;width:717px;height:249px;background:var(--navy)}
.news-title{left:0;top:994px;width:717px;text-align:center;font-family:Oswald,sans-serif;font-size:18px;font-weight:500;color:var(--white)}
.news-input{left:204px;top:1026px;width:250px;height:26px;background:var(--white);border-radius:13px 0 0 13px;font-size:6.5px;color:var(--muted);padding:9px 17px}
.footer-brand{left:0;top:1084px;width:717px;justify-content:center;font-size:15px;color:var(--white)}
.footer-brand .brand-dot{background:var(--blue-bright)}
.rule{left:81px;width:555px;height:1px;background:#3a4058}
.foot-nav a{position:absolute;top:1141px;font-family:Oswald,sans-serif;font-size:8.5px;font-weight:500;color:var(--white);text-decoration:none}
.foot-nav a.current{color:var(--blue-bright)}
.legal{top:1172px;font-size:6.5px;color:#8a90a4}
</style>
</head>
<body>
<header class="abs site-header">
  <div class="abs brand header-brand"><span class="brand-dot"></span>Brightwater Systems</div>
  <nav class="nav">
    <a style="left:322px" href="#">HOME</a>
    <a style="left:379px" href="#">ABOUT US</a>
    <a style="left:449px" href="#">OUR SERVICES</a>
    <a style="left:533px" href="#">BLOG</a>
    <a style="left:587px" href="#">CONTACT US</a>
  </nav>
  <div class="abs nav-active"></div>
</header>

<section class="abs hero" role="img" aria-label="Blue banner with a faint dotted world map"></section>
<p class="abs hero-kicker">GET IN TOUCH</p>
<h1 class="abs hero-title">WANT TO CHAT WITH US TO GET TO KNOW US BETTER?</h1>

<div class="ornament ornament-square" role="img" aria-label="Decorative dotted grid"></div>
<div class="ornament ornament-tri" role="img" aria-label="Decorative dotted triangle"></div>

<div class="abs form-card"></div>
<div class="abs form-frame"></div>
<div class="field" style="left:125px;top:246px;width:229px;height:24px">Name</div>
<div class="field" style="left:363px;top:246px;width:229px;height:24px">Email</div>
<div class="field" style="left:125px;top:281px;width:229px;height:24px">Business name</div>
<div class="field" style="left:363px;top:281px;width:229px;height:24px">Phone Number</div>
<div class="field" style="left:125px;top:315px;width:467px;height:78px">Message</div>
<div class="abs captcha">
  <span class="abs captcha-box"></span>
  <span class="abs captcha-label">I'm not a robot</span>
  <span class="abs captcha-mark"></span>
  <span class="abs captcha-note">Verify check<br>Privacy</span>
</div>
<div class="btn" style="left:323px;top:455px;width:71px;height:22px">SUBMIT</div>

<section class="abs contact-band"></section>
<div class="info-card" style="left:81px">
  <div class="info-icon"><svg width="11" height="11" viewBox="0 0 24 24"><path fill="#fff" d="M6.6 10.8a15.1 15.1 0 0 0 6.6 6.6l2.2-2.2a1 1 0 0 1 1-.25 11.4 11.4 0 0 0 3.6.57 1 1 0 0 1 1 1V20a1 1 0 0 1-1 1A17 17 0 0 1 3 4a1 1 0 0 1 1-1h3.5a1 1 0 0 1 1 1c0 1.25.2 2.45.57 3.57a1 1 0 0 1-.25 1z"/></svg></div>
  <div class="info-title">PHONE NUMBER</div>
  <div class="info-text">+0044 555-010-2040<br>+0044 555-010-2040</div>
</div>
<div class="info-card" style="left:226px">
  <div class="info-icon"><svg width="11" height="9" viewBox="0 0 22 16"><rect width="22" height="16" fill="#fff"/><path d="M1 1l10 8 10-8" stroke="#0557a5" stroke-width="1.6" fill="none"/></svg></div>
  <div class="info-title">EMAIL ADDRESS</div>
  <div class="info-text">info@brightwatersys.com<br>sales@brightwatersys.com</div>
</div>
<div class="info-card" style="left:365px">
  <div class="info-icon"><svg width="9" height="12" viewBox="0 0 18 24"><path fill="#fff" d="M9 0a9 9 0 0 0-9 9c0 7 9 15 9 15s9-8 9-15a9 9 0 0 0-9-9zm0 12a3 3 0 1 1 0-6 3 3 0 0 1 0 6z"/></svg></div>
  <div class="info-title">ADDRESS</div>
  <div class="info-text" style="line-height:11px">Location Town, City name ,<br>Country</div>
</div>
<div class="info-card" style="left:511px">
  <div class="info-icon"><svg width="14" height="12" viewBox="0 0 24 21"><path fill="#fff" d="M12 21l-1.7-1.6C4.2 13.9 0 10.1 0 5.6 0 2.4 2.5 0 5.6 0c1.9 0 3.6.9 4.7 2.3h3.4C14.8.9 16.5 0 18.4 0 21.5 0 24 2.4 24 5.6c0 4.5-4.2 8.3-10.3 13.8z"/></svg></div>
  <div class="info-title">FOLLOW US</div>
  <div class="social"><span>Pix</span><span>Chat</span><span>Feed</span><span>Net</span></div>
</div>

<div class="abs map" role="img" aria-label="Street map showing the office location downtown"></div>

<footer class="abs footer"></footer>
<h2 class="abs news-title">OUR NEWS LETTER</h2>
<div class="abs news-input">johndoe@clientemailid.com</div>
<div class="btn" style="left:442px;top:1026px;width:72px;height:26px;border-radius:13px">SUBMIT</div>
<div class="abs brand footer-brand"><span class="brand-dot"></span>Brightwater Systems</div>
<div class="abs rule" style="top:1131px"></div>
<nav class="foot-nav">
  <a style="left:205px" href="#">HOME</a>
  <a style="left:262px" href="#">ABOUT US</a>
  <a style="left:332px" href="#">OUR SERVICES</a>
  <a style="left:416px" href="#">BLOG</a>
  <a class="current" style="left:471px" href="#">CONTACT US</a>
</nav>
<div class="abs rule" style="top:1165px"></div>
<p class="abs legal" style="left:81px">COPYRIGHT © 2021 BRIGHTWATER SYSTEMS</p>
<p class="abs legal" style="left:503px">PRIVACY POLICY &nbsp;| TERMS OF SERVICES</p>
</body>
</html>
```